Business Card Design Wenda Style

I make Hand Made Name necklaces which are known as Wenda Style and would like a Shiny Gold Business Card almost to look like a Gold Bar.
on the 2nd side I want an image of a Wenda Necklace in Silver as it will be on a Gold Background.

Industry/Entity Type

Business

Contact Information for Business Card

Dunvok Jewellery UK
Loop Pendants 2 Go

Hugo Penwright
Director
M: 07700 914 263

www.dunvokjwl.co.uk

Requirements
Must have
• Writing must be in Black

Card must be metallic gold

```html
<!DOCTYPE html>
<html lang="en">
<head>
<meta charset="utf-8">
<title>Dunvok Jewellery UK – Business Card</title>
<link href="https://fonts.googleapis.com/css2?family=Questrial&display=swap" rel="stylesheet">
<style>
  :root {
    --backdrop: #ece6dc;
    --gold-light: #f2b34a;
    --gold-mid: #d98a18;
    --gold-deep: #a8620a;
    --gold-edge: #8a4f08;
    --ink: #111111;
    --ink-soft: #2a2a2a;
    --silver-light: #f4f4f2;
    --silver-mid: #cfcfcb;
    --silver-deep: #9c9c98;
  }
  * { margin: 0; padding: 0; box-sizing: border-box; }
  html, body {
    width: 1200px;
    height: 784px;
    overflow: hidden;
    background: var(--backdrop);
  }
  .canvas {
    position: relative;
    width: 1200px;
    height: 784px;
    font-family: "Questrial", "Century Gothic", sans-serif;
  }
  .card {
    position: absolute;
    width: 560px;
    height: 320px;
    border-radius: 4px;
    overflow: hidden;
    background:
      linear-gradient(100deg, rgba(255,255,255,0.18) 0%, rgba(255,255,255,0) 35%, rgba(255,255,255,0.12) 60%, rgba(0,0,0,0.08) 100%),
      linear-gradient(180deg, var(--gold-light) 0%, var(--gold-mid) 55%, var(--gold-deep) 100%);
    box-shadow: 0 10px 26px rgba(60, 35, 5, 0.28);
  }
  .card--front { left: 40px; top: 70px; }
  .card--back  { left: 600px; top: 394px; }

  /* Front: necklace feature */
  .necklace-chain {
    position: absolute;
    left: 0;
    top: 0;
    width: 560px;
    height: 320px;
  }
  .necklace-feature {
    position: absolute;
    left: 70px;
    top: 70px;
    width: 420px;
    height: 130px;
    border-radius: 60px;
    background: radial-gradient(ellipse at 45% 40%, var(--silver-light) 0%, var(--silver-mid) 60%, var(--silver-deep) 100%);
    box-shadow: 2px 4px 6px rgba(70, 40, 5, 0.35);
  }

  /* Back: brand + contact */
  .brand {
    position: absolute;
    left: 36px;
    top: 34px;
    display: flex;
    align-items: center;
    gap: 14px;
  }
  .brand-mark {
    width: 58px;
    height: 58px;
    border-radius: 50%;
    background: var(--ink);
  }
  .brand-name {
    font-size: 30px;
    line-height: 1;
    color: var(--ink);
  }
  .brand-tagline {
    position: absolute;
    left: 108px;
    top: 84px;
    font-size: 14px;
    letter-spacing: 0.3px;
    color: var(--ink-soft);
  }
  .necklace-watermark {
    position: absolute;
    left: 250px;
    top: 115px;
    width: 280px;
    height: 90px;
    border-radius: 45px;
    background: radial-gradient(ellipse at center, rgba(255,255,255,0.10) 0%, rgba(255,255,255,0) 70%);
  }
  .contact {
    position: absolute;
    left: 40px;
    top: 178px;
    color: var(--ink);
  }
  .contact-name {
    font-size: 22px;
    line-height: 1.1;
  }
  .contact-role {
    font-size: 14px;
    color: var(--ink-soft);
    margin-bottom: 18px;
  }
  .contact-line {
    display: flex;
    align-items: center;
    gap: 12px;
    font-size: 21px;
    line-height: 1.5;
  }
  .contact-icon {
    width: 20px;
    height: 20px;
    flex: none;
  }
</style>
</head>
<body>
<main class="canvas">

  <section class="card card--front">
    <svg class="necklace-chain" viewBox="0 0 560 320" aria-hidden="true">
      <path d="M40 0 L78 118" stroke="#e6e6e2" stroke-width="3" fill="none"/>
      <path d="M520 0 L482 118" stroke="#e6e6e2" stroke-width="3" fill="none"/>
    </svg>
    <div class="necklace-feature" role="img" aria-label="Silver Wenda name necklace in script lettering on a fine chain"></div>
  </section>

  <section class="card card--back">
    <div class="necklace-watermark" role="img" aria-label="Faint Wenda necklace lettering in the background"></div>

    <div class="brand">
      <span class="brand-mark"></span>
      <span class="brand-name">Dunvok Jewellery UK</span>
    </div>
    <p class="brand-tagline">Loop Pendants 2 Go</p>

    <div class="contact">
      <p class="contact-name">Hugo Penwright</p>
      <p class="contact-role">Director</p>
      <p class="contact-line">
        <svg class="contact-icon" viewBox="0 0 24 24" aria-hidden="true">
          <path fill="#111" d="M6.6 10.8a15.1 15.1 0 0 0 6.6 6.6l2.2-2.2a1 1 0 0 1 1-.25 11.4 11.4 0 0 0 3.6.57 1 1 0 0 1 1 1V20a1 1 0 0 1-1 1A17 17 0 0 1 3 4a1 1 0 0 1 1-1h3.5a1 1 0 0 1 1 1c0 1.25.2 2.45.57 3.57a1 1 0 0 1-.25 1z"/>
        </svg>
        <span>07700 914 263</span>
      </p>
      <p class="contact-line">
        <svg class="contact-icon" viewBox="0 0 24 24" aria-hidden="true">
          <circle cx="12" cy="12" r="10" fill="#111"/>
          <g stroke="#d98a18" stroke-width="1.3" fill="none">
            <ellipse cx="12" cy="12" rx="4.2" ry="9.6"/>
            <line x1="2" y1="12" x2="22" y2="12"/>
            <path d="M4 7h16M4 17h16"/>
          </g>
        </svg>
        <span>www.dunvokjwl.co.uk</span>
      </p>
    </div>
  </section>

</main>
</body>
</html>
```